Fashion Site

I need a Home Page and one Internal Page (About or Stores you choose) for a Fashion Retailer called VERANO based in Melbourne Australia. Their product range is high end - European brand (i.e. Corvelli, Batrano etc) shoes, handbags and accessories for Women and Men (Customers 75% Women 25% Men). They currently have a site at www.verano-shoes.com.au (My developer will take this design and push it through the rest of the site).

The new design will be clean and modern and reflect the high end brands they sell. The finished site will have the home page plus the following pages - About - Stores - News/Sales - E-Shop - Contact with links to Join our mail list - Chatterly - Pixelane. I would like a main banner/slider at the top that will have 6 sliding images - through these images I would like to reinforce the following - the products are imported direct from Italy and are the latest most current designs from leading fashion houses (women and men) - A Modern Look with an Italian feel. Then we would also like to show some products/specials from the new E-Shop on the home page as well as the usual links etc.

Their colours are black and white but I am open to having a splash of colour and a must is to use the photography supplied in a creative way (see http://dunestrive.com as an Idea), we want to show that the products are high end - hand made. Their end/tag line is Ever Poised. We DO NOT want any brand names mentioned/Listed (if on a photo that is fine). The site will need to be easy to navigate and google friendly so please keep this in mind with the design. The images supplied include: Product Shots, Melbourne Stores, Italy Warehouse (2 story building with red roof) and Italy Factories/Craftsmen.

Target Market(s)

Fashion Conscious Women and Men who like the finer things in life

Industry/Entity Type

Fashion

Font styles to use
Serif
Sans Serif

Requirements
Must have
• Top Banner with 6 Images that Slide/Scroll in a banner.
Nice to have
• See the Following Sites that may inspire:
https://www.koti.com.au
http://www.fennicraft.co (the Look not the colours)
http://www.tobsandyou.com
Also Like the banner in this http://dunestrive.com (Just the banner)

```html
<!DOCTYPE html>
<html lang="en">
<head>
<meta charset="utf-8">
<title>VERANO — Home</title>
<link href="https://fonts.googleapis.com/css2?family=Source+Sans+3:wght@300;400;600;700&family=Oswald:wght@500&display=swap" rel="stylesheet">
<style>
:root{
  --ink:#111;
  --text:#333;
  --muted:#666;
  --line:#dcdcdc;
  --paper:#fff;
  --yellow:#f7e20a;
  --olive:#c9b520;
  --wine:#86223a;
  --btn-border:#d6d6d6;
}
*{box-sizing:border-box;margin:0;padding:0}
html,body{width:1008px;height:1200px;overflow:hidden;background:var(--paper)}
body{position:relative;font-family:"Source Sans 3",Arial,sans-serif;color:var(--text)}
.abs{position:absolute}

/* utility bar */
.utility-bar{left:0;top:0;width:1008px;height:28px;background:var(--ink);color:#ddd;font-size:9px}
.utility-bar a{position:absolute;top:9px;color:#ccc;text-decoration:none}
.utility-bar .cart-total{position:absolute;left:758px;top:0;height:28px;width:58px;border-left:1px solid #444;color:#fff;font-weight:600;padding:9px 0 0 12px}
.utility-bar .cart-btn{position:absolute;left:816px;top:0;width:32px;height:28px;background:#3a3a3a}
.utility-bar .search-btn{position:absolute;left:848px;top:0;width:32px;height:28px}

/* header */
.site-header{left:0;top:28px;width:1008px;height:96px;border-bottom:1px solid #e4e4e4}
.main-nav a{position:absolute;top:38px;font-size:14px;font-weight:300;color:#555;text-decoration:none}
.main-nav a.current{color:var(--ink);font-weight:400;border-bottom:1px solid var(--ink);padding-bottom:1px}
.brand{position:absolute;left:454px;top:12px;width:100px;text-align:center}
.brand .tag{font-size:9.5px;color:#777;font-weight:300}
.brand .name{font-size:30px;font-weight:700;color:var(--ink);letter-spacing:-1px;line-height:38px}

/* hero slider */
.hero{left:128px;top:139px;width:752px;height:320px;border:1px solid #ddd;padding:7px;background:#fff}
.hero .slide{width:100%;height:100%;background:linear-gradient(135deg,#7a5a48 0%,#3f4350 35%,#2f333d 60%,#8a6e5c 100%);position:relative}
.hero h2{position:absolute;left:23px;top:228px;font-family:Oswald,sans-serif;font-weight:500;font-size:25px;color:var(--yellow);letter-spacing:.5px}
.hero .rule{position:absolute;left:23px;top:257px;width:226px;height:1px;background:var(--yellow)}
.hero p{position:absolute;left:23px;top:262px;font-size:12px;color:#fff}
.hero-shadow{left:200px;top:459px;width:608px;height:10px;background:radial-gradient(ellipse at top,rgba(0,0,0,.18),transparent 70%)}

/* categories */
.category{top:483px;width:251px;height:176px}
.category .photo{height:136px}
.category .band{height:40px;padding:4px 0 0 16px;color:#fff;position:relative}
.category .band h3{font-size:14px;font-weight:400}
.category .band p{font-size:8.5px;font-weight:600;margin-left:2px}
.category .band svg{position:absolute;right:28px;top:14px}

/* featured */
.section-title{left:127px;top:681px;font-size:12.5px;color:var(--ink)}
.section-rule{left:128px;top:704px;width:752px;height:1px;background:var(--line)}
.product{top:738px;width:176px}
.product .photo{height:96px}
.product h4{font-size:10.5px;font-weight:400;line-height:16px;margin-top:8px;color:var(--text)}
.product .divider{height:1px;background:var(--line);margin-top:8px}
.product .price{font-size:10.5px;font-weight:600;color:var(--ink);margin-top:5px}
.product .actions{display:flex;margin-top:5px;height:28px;border:1px solid var(--btn-border)}
.product .actions .cart{width:32px;background:var(--ink);display:flex;align-items:center;justify-content:center;margin:-1px 0 -1px -1px}
.product .actions .add{width:79px;font-size:8px;color:#555;display:flex;align-items:center;padding-left:10px;border-right:1px solid var(--btn-border)}
.product .actions .ico{width:32px;display:flex;align-items:center;justify-content:center;border-right:1px solid var(--btn-border)}
.product .actions .ico:last-child{border-right:none}

/* footer */
.footer-rule{left:128px;top:968px;width:752px;height:1px;background:var(--line)}
.footer-brand{left:128px;top:984px;font-size:30px;font-weight:700;color:var(--ink);letter-spacing:-1px}
.footer-col{top:1049px;width:176px;font-size:10px;color:#555;line-height:16px}
.footer-col h5{font-size:12px;font-weight:600;color:var(--ink);height:20px;border-bottom:1px solid var(--line);margin-bottom:6px;display:flex;align-items:center;gap:7px}
.footer-col .phone{display:flex;gap:5px;margin-top:8px}
.social{display:flex;gap:12px;margin-top:8px;font-size:11px;font-weight:600;color:#3b5a9a}
.social span{display:flex;align-items:center;gap:5px}
.social i{display:inline-block;width:14px;height:14px;background:#3b5a9a}
.social span.alt{color:#999}
.social span.alt i{background:#bbb}
.copyright-bar{left:0;top:1164px;width:1008px;height:36px;background:var(--ink);color:#fff;font-size:10px;font-weight:600;padding:12px 0 0 128px}
</style>
</head>
<body>

<div class="abs utility-bar">
  <a style="left:128px">My Account</a>
  <a style="left:189px">Shopping cart</a>
  <a style="left:257px">Check out</a>
  <a style="left:671px">Sign in</a>
  <a style="left:713px">Register</a>
  <div class="cart-total">$ 0.00 (0)</div>
  <div class="cart-btn"><svg width="32" height="28" viewBox="0 0 32 28"><path d="M10 9h2l2 7h7l2-5h-10" fill="none" stroke="#aaa" stroke-width="1.5"/><circle cx="14.5" cy="18.5" r="1.2" fill="#aaa"/><circle cx="20" cy="18.5" r="1.2" fill="#aaa"/></svg></div>
  <div class="search-btn"><svg width="32" height="28" viewBox="0 0 32 28"><circle cx="14" cy="12.5" r="4.5" fill="none" stroke="#f7e20a" stroke-width="2"/><path d="M17.5 16l4 4" stroke="#f7e20a" stroke-width="2.4"/></svg></div>
</div>

<header class="abs site-header">
  <nav class="main-nav">
    <a class="current" style="left:144px">Home</a>
    <a style="left:233px">About Us</a>
    <a style="left:341px">Stores</a>
    <a style="left:577px">News/Sales</a>
    <a style="left:702px">E-Shop</a>
    <a style="left:799px">Contact Us</a>
  </nav>
  <div class="brand"><div class="tag">Ever Poised</div><div class="name">VERANO</div></div>
</header>

<section class="abs hero">
  <div class="slide" role="img" aria-label="Photograph: hands holding a dark leather insole stamped Made in Italy">
    <h2>MADE IN ITALY</h2>
    <div class="rule"></div>
    <p>Direct from italy Ladies, mens and kids footware</p>
  </div>
</section>
<div class="abs hero-shadow"></div>

<a class="abs category" style="left:128px">
  <div class="photo" role="img" aria-label="Black and white photograph of a men's leather loafer" style="background:linear-gradient(160deg,#9a9a9a,#3a3a3a 55%,#bdbdbd)"></div>
  <div class="band" style="background:var(--ink)"><h3>Mens Shoes</h3><p>Sed ut perspiciatis unde omnis iste natus</p>
  <svg width="8" height="12" viewBox="0 0 8 12"><path d="M1.5 1.5l4.5 4.5-4.5 4.5" fill="none" stroke="#fff" stroke-width="2"/></svg></div>
</a>
<a class="abs category" style="left:379px">
  <div class="photo" role="img" aria-label="Photograph of black suede women's heels on marble" style="background:linear-gradient(180deg,#e8e8e8,#6a6a6a 45%,#d8d8d8)"></div>
  <div class="band" style="background:var(--olive)"><h3>Womens Shoes</h3><p>Sed ut perspiciatis unde omnis iste natus</p>
  <svg width="8" height="12" viewBox="0 0 8 12"><path d="M1.5 1.5l4.5 4.5-4.5 4.5" fill="none" stroke="#fff" stroke-width="2"/></svg></div>
</a>
<a class="abs category" style="left:630px">
  <div class="photo" role="img" aria-label="Black and white photograph of a store front" style="background:linear-gradient(90deg,#555,#222 50%,#777)"></div>
  <div class="band" style="background:var(--wine)"><h3>Hand Bags</h3><p>Sed ut perspiciatis unde omnis iste natus</p>
  <svg width="8" height="12" viewBox="0 0 8 12"><path d="M1.5 1.5l4.5 4.5-4.5 4.5" fill="none" stroke="#fff" stroke-width="2"/></svg></div>
</a>

<h2 class="abs section-title">FEATURED PRODUCTS</h2>
<svg class="abs" style="left:855px;top:683px" width="26" height="12" viewBox="0 0 26 12"><path d="M5 1.5L1.5 6 5 10.5" fill="none" stroke="#aaa" stroke-width="1.5"/><path d="M20 1.5L24 6l-4 4.5" fill="none" stroke="#111" stroke-width="2"/></svg>
<div class="abs section-rule"></div>

<article class="abs product" style="left:128px">
  <div class="photo" role="img" aria-label="Photograph of a metallic green ballet flat" style="background:radial-gradient(ellipse at 50% 60%,#8fa83a,#c9cdbf 55%,#e9e9e6)"></div>
  <h4>At vero eos et accusamus et iusto odio dignissimos ducimus</h4><div class="divider"></div>
  <div class="price">$ 120.00</div>
  <div class="actions"><div class="cart"><svg width="12" height="10" viewBox="0 0 12 10"><path d="M0 1h2l1.5 5h6l1.5-4H3" fill="none" stroke="#fff" stroke-width="1.3"/><circle cx="4" cy="8.5" r="1" fill="#fff"/><circle cx="9" cy="8.5" r="1" fill="#fff"/></svg></div><div class="add">ADD TO CART</div><div class="ico"><svg width="12" height="11" viewBox="0 0 12 11"><path d="M6 10L1 5a2.7 2.7 0 015-3.3A2.7 2.7 0 0111 5z" fill="#999"/></svg></div><div class="ico"><svg width="12" height="12" viewBox="0 0 12 12"><path d="M2 5a4 4 0 017-2M10 7a4 4 0 01-7 2" fill="none" stroke="#999" stroke-width="1.4"/><path d="M9 0.5v3H6M3 11.5v-3h3" fill="none" stroke="#999" stroke-width="1.4"/></svg></div></div>
</article>
<article class="abs product" style="left:320px">
  <div class="photo" role="img" aria-label="Photograph of navy and blue suede loafers" style="background:radial-gradient(ellipse at 50% 55%,#3a4e8c,#a3a8b4 55%,#ececec)"></div>
  <h4>At vero eos et accusamus et iusto odio dignissimos ducimus</h4><div class="divider"></div>
  <div class="price">$ 140.00</div>
  <div class="actions"><div class="cart"><svg width="12" height="10" viewBox="0 0 12 10"><path d="M0 1h2l1.5 5h6l1.5-4H3" fill="none" stroke="#fff" stroke-width="1.3"/><circle cx="4" cy="8.5" r="1" fill="#fff"/><circle cx="9" cy="8.5" r="1" fill="#fff"/></svg></div><div class="add">ADD TO CART</div><div class="ico"><svg width="12" height="11" viewBox="0 0 12 11"><path d="M6 10L1 5a2.7 2.7 0 015-3.3A2.7 2.7 0 0111 5z" fill="#999"/></svg></div><div class="ico"><svg width="12" height="12" viewBox="0 0 12 12"><path d="M2 5a4 4 0 017-2M10 7a4 4 0 01-7 2" fill="none" stroke="#999" stroke-width="1.4"/><path d="M9 0.5v3H6M3 11.5v-3h3" fill="none" stroke="#999" stroke-width="1.4"/></svg></div></div>
</article>
<article class="abs product" style="left:512px">
  <div class="photo" role="img" aria-label="Photograph of red and yellow patent flats" style="background:linear-gradient(100deg,#e9e9e9 10%,#d8262b 40%,#e8c92a 75%,#2b3550)"></div>
  <h4>At vero eos et accusamus et iusto odio dignissimos ducimus</h4><div class="divider"></div>
  <div class="price">$ 100.00</div>
  <div class="actions"><div class="cart"><svg width="12" height="10" viewBox="0 0 12 10"><path d="M0 1h2l1.5 5h6l1.5-4H3" fill="none" stroke="#fff" stroke-width="1.3"/><circle cx="4" cy="8.5" r="1" fill="#fff"/><circle cx="9" cy="8.5" r="1" fill="#fff"/></svg></div><div class="add">ADD TO CART</div><div class="ico"><svg width="12" height="11" viewBox="0 0 12 11"><path d="M6 10L1 5a2.7 2.7 0 015-3.3A2.7 2.7 0 0111 5z" fill="#999"/></svg></div><div class="ico"><svg width="12" height="12" viewBox="0 0 12 12"><path d="M2 5a4 4 0 017-2M10 7a4 4 0 01-7 2" fill="none" stroke="#999" stroke-width="1.4"/><path d="M9 0.5v3H6M3 11.5v-3h3" fill="none" stroke="#999" stroke-width="1.4"/></svg></div></div>
</article>
<article class="abs product" style="left:704px">
  <div class="photo" role="img" aria-label="Photograph of blue and red leather driving loafers" style="background:linear-gradient(100deg,#f0f0f0 5%,#2f5ea8 35%,#c8312c 70%,#f0f0f0)"></div>
  <h4>At vero eos et accusamus et iusto odio dignissimos ducimus</h4><div class="divider"></div>
  <div class="price">$ 120.00</div>
  <div class="actions"><div class="cart"><svg width="12" height="10" viewBox="0 0 12 10"><path d="M0 1h2l1.5 5h6l1.5-4H3" fill="none" stroke="#fff" stroke-width="1.3"/><circle cx="4" cy="8.5" r="1" fill="#fff"/><circle cx="9" cy="8.5" r="1" fill="#fff"/></svg></div><div class="add">ADD TO CART</div><div class="ico"><svg width="12" height="11" viewBox="0 0 12 11"><path d="M6 10L1 5a2.7 2.7 0 015-3.3A2.7 2.7 0 0111 5z" fill="#999"/></svg></div><div class="ico"><svg width="12" height="12" viewBox="0 0 12 12"><path d="M2 5a4 4 0 017-2M10 7a4 4 0 01-7 2" fill="none" stroke="#999" stroke-width="1.4"/><path d="M9 0.5v3H6M3 11.5v-3h3" fill="none" stroke="#999" stroke-width="1.4"/></svg></div></div>
</article>

<div class="abs footer-rule"></div>
<div class="abs footer-brand">VERANO</div>

<div class="abs footer-col" style="left:128px">
  <h5><svg width="8" height="12" viewBox="0 0 8 12"><path d="M4 12L0.8 5.5A3.6 3.6 0 117.2 5.5z" fill="#111"/><circle cx="4" cy="4" r="1.4" fill="#fff"/></svg>Address</h5>
  <p>CITY - 4 Stores at 88 Laurel St (inside Arbell House) Melbourne VIC 3000.</p>
  <div class="phone"><svg width="11" height="11" viewBox="0 0 11 11"><path d="M2 0.5l2 2.5-1 1.5a6 6 0 003.5 3.5L8 7l2.5 2-1 1.5C5 10.5 0.5 6 0.5 1.5z" fill="#333"/></svg><div>(03) 9555 0141 (ladies boutique)<br>(03) 9555 0187 (mens boutique)</div></div>
</div>
<div class="abs footer-col" style="left:320px">
  <h5><svg width="8" height="12" viewBox="0 0 8 12"><path d="M4 12L0.8 5.5A3.6 3.6 0 117.2 5.5z" fill="#111"/><circle cx="4" cy="4" r="1.4" fill="#fff"/></svg>Outlet Address</h5>
  <p>22/410 Wexbury Rd Ashvale VIC 3163.</p>
  <div class="phone"><svg width="11" height="11" viewBox="0 0 11 11"><path d="M2 0.5l2 2.5-1 1.5a6 6 0 003.5 3.5L8 7l2.5 2-1 1.5C5 10.5 0.5 6 0.5 1.5z" fill="#333"/></svg><div>(03) 9555 0163</div></div>
</div>
<div class="abs footer-col" style="left:512px">
  <h5>Customer Care</h5>
  <p>Frequently Asked Questions<br>Privacy &amp; Security<br>Shipping &amp; Returns<br>Terms of Service</p>
</div>
<div class="abs footer-col" style="left:704px">
  <h5>Follow us</h5>
  <div class="social"><span><i></i>Chatterly</span><span class="alt"><i></i>Pixelane</span></div>
</div>

<footer class="abs copyright-bar">Copy rights ©2014 VERANO</footer>

</body>
</html>
```